Venlox - Property Management Company Listings - PSD / uncoded only

Our site simply connects property owners with property managers. I’m asking you to create 2 pages, 1 homepage and 1 page that lists of property management companies. Build with Responsive Design in mind. PSD/uncoded files only. Help us create a great site!
Example competitor sites:
http://www.everyestatehelp.example/
http://www.tendyourlots.example/
Inspired by these sites:
http://www.quorvik.example/
http://www.bespokely.example/
http://www.coinwire.example/
https://www.tripboard.example/
I've attached the logo as well as 2 picture files that you can consider using.
• Venlox Logo Colors: Yellow: HTML code: #FBC30A, RGB code: R: 251 G: 195 B: 10 Grey: HTML code: #4E4C4D, RGB code: R: 78 G: 76 B: 77
• The picture files are optional.
o One picture is of houses and neighborhood.
o The other is of a professional woman on the phone. Please do not use the professional woman as a large primary image. You can use the professional woman photo as a smaller photo and not the main photo.
• Please bring your own pictures and graphics too. Don't feel like you need to use mine.
Thank you!

```html
<!DOCTYPE html>
<html lang="en">
<head>
<meta charset="utf-8">
<title>Venlox – Property Management Solutions</title>
<link href="https://fonts.googleapis.com/css2?family=Open+Sans:wght@300;400;600&display=swap" rel="stylesheet">
<style>
:root{
  --yellow:#fbc30a;
  --grey:#4e4c4d;
  --ink:#333333;
  --text:#4a4a4a;
  --page:#f2f2f2;
  --panel:#c9c9c9;
  --footer:#2d2d2d;
  --white:#ffffff;
}
*{box-sizing:border-box;margin:0;padding:0}
html,body{width:1069px;height:1200px;overflow:hidden}
body{position:relative;font-family:"Open Sans",Arial,sans-serif;background:var(--page);color:var(--text)}
.abs{position:absolute}

.top-bar{left:0;top:0;width:1069px;height:23px;background:var(--yellow);font-size:13px;color:var(--ink)}
.top-bar .item{position:absolute;top:3px;display:flex;align-items:center;gap:7px;white-space:nowrap}
.top-bar svg{width:12px;height:12px;fill:var(--ink)}

.site-header{left:0;top:23px;width:1069px;height:69px;background:var(--white)}
.brand{position:absolute;left:44px;top:19px;display:flex;align-items:center;gap:6px}
.brand-mark{width:10px;height:10px;background:var(--yellow)}
.brand-name{font-size:25px;font-weight:600;color:var(--grey);line-height:1;white-space:nowrap}
.brand-tag{position:absolute;left:154px;top:14px;font-size:17px;font-weight:600;color:var(--grey);line-height:20px;white-space:nowrap}
.brand-tag span{display:block;padding-left:8px;font-size:16px}
.main-nav{position:absolute;top:24px;font-size:16px;color:var(--ink);white-space:nowrap}

.hero{left:0;top:92px;width:1069px;height:424px;
  background:linear-gradient(180deg,#9fc4e4 0%,#b6614a 30%,#a55742 58%,#5f8a3a 82%,#4f7d2c 100%)}
.hero-caption{position:absolute;left:64px;top:114px;width:504px;height:63px;background:rgba(60,60,60,.82);
  color:var(--yellow);font-size:18px;padding:0 14px;line-height:63px;white-space:nowrap;overflow:hidden}

.pm-heading{left:0;top:542px;width:1069px;text-align:center;font-size:29px;font-weight:400;color:var(--ink);letter-spacing:.5px}
.pm-intro{left:0;top:610px;width:1069px;text-align:center;font-size:20px;font-weight:300;color:var(--ink);line-height:29px}

.btn{position:absolute;background:var(--yellow);color:var(--ink);font-size:19px;font-weight:300;
  display:flex;align-items:center;justify-content:center;gap:12px;white-space:nowrap}
.btn svg{width:13px;height:13px;fill:var(--ink)}

.search-panel{left:36px;top:761px;width:488px;height:291px;background:var(--panel);border:2px solid var(--yellow)}
.panel-title{position:absolute;font-size:19px;color:var(--ink)}
.field-label{position:absolute;top:70px;font-size:16px;line-height:22px;color:var(--ink);white-space:nowrap}
.select{position:absolute;left:27px;top:98px;width:257px;height:37px;background:var(--white);border:1px solid #555;
  font-size:12.5px;color:#111;padding:0 20px 0 5px;line-height:35px;white-space:nowrap;overflow:hidden}
.select svg{position:absolute;right:6px;top:14px;width:11px;height:7px;fill:#333}
.zip{position:absolute;left:294px;top:98px;width:162px;height:37px;background:var(--white);border:1px solid #555}
.panel-note{position:absolute;left:27px;top:210px;width:430px;font-size:16px;line-height:20px;color:var(--ink)}

.steps-panel{left:545px;top:761px;width:487px;height:291px;background:var(--white);border:2px solid var(--yellow)}
.steps{position:absolute;left:18px;top:94px;list-style:none;font-size:15px;color:var(--text)}
.steps li{height:33.5px;white-space:nowrap}

.site-footer{left:0;top:1130px;width:1069px;height:70px;background:var(--footer);border-top:2px solid var(--yellow)}
.copyright{position:absolute;left:64px;top:27px;font-size:12px;color:var(--white);white-space:nowrap}
.footer-links{position:absolute;left:590px;top:18px;width:460px;font-size:12px;line-height:17px;color:var(--yellow);list-style:none}
.footer-links li{display:inline-block;margin-right:8px;white-space:nowrap}
.footer-links li::before{content:"";display:inline-block;width:6px;height:6px;border-radius:50%;background:var(--white);margin-right:9px;vertical-align:2px}
.footer-links .row-break{display:block;height:0;margin:0}
.footer-links .row-break::before{display:none}
</style>
</head>
<body>

<div class="abs top-bar">
  <div class="item" style="left:846px">
    <svg viewBox="0 0 12 12"><circle cx="6" cy="3.5" r="3"/><path d="M0 12c0-4 2.5-5.5 6-5.5S12 8 12 12z"/></svg>Login
  </div>
  <div class="item" style="left:928px">
    <svg viewBox="0 0 12 12"><path d="M2.5 0.5l2 2.5-1.2 1.5c.8 1.7 2.2 3.1 3.9 3.9l1.5-1.2 2.5 2-1.3 2.3C4.6 11.3.7 7.4.2 2z"/></svg>555 014 2261
  </div>
</div>

<header class="abs site-header">
  <div class="brand"><span class="brand-mark"></span><span class="brand-name">Venlox</span></div>
  <div class="brand-tag">Property Management Solutions<span>Simplified.</span></div>
  <nav>
    <span class="main-nav" style="left:645px">Home</span>
    <span class="main-nav" style="left:712px">Are you a Property&nbsp; Manager</span>
    <span class="main-nav" style="left:939px">Contact Us</span>
  </nav>
</header>

<section class="abs hero" role="img" aria-label="Photo of a red brick two-storey house with white shutters, garage, shrubs and a green lawn under a blue sky">
  <div class="hero-caption">Providing property management solutions, simplified.</div>
</section>

<h1 class="abs pm-heading">ARE YOU A PROPERTY MANAGER?</h1>
<p class="abs pm-intro">Join our real estate property management company network.<br>Let us help you find leads of property owners seeking to rent their homes</p>
<a class="btn" style="left:462px;top:688px;width:144px;height:40px">Learn More
  <svg viewBox="0 0 12 12"><path d="M1 0l11 6-11 6z"/></svg></a>

<section class="abs search-panel">
  <h2 class="panel-title" style="left:27px;top:26px;font-weight:400">Find your Local Property Manager</h2>
  <span class="field-label" style="left:27px">Select Property Type:</span>
  <span class="field-label" style="left:294px">In Zipcode:</span>
  <div class="select">Single Home or Condo ($300 to $500K)
    <svg viewBox="0 0 11 7"><path d="M0 0h11L5.5 7z"/></svg></div>
  <div class="zip"></div>
  <a class="btn" style="left:187px;top:163px;width:126px;height:35px">Search
    <svg viewBox="0 0 14 14"><circle cx="5.5" cy="5.5" r="4.2" fill="none" stroke="#333" stroke-width="2"/><path d="M8.5 8.5l4.5 4.5" stroke="#333" stroke-width="2.4"/></svg></a>
  <p class="panel-note">Search our directory to find experienced and professional property management companies that meet your needs.</p>
</section>

<section class="abs steps-panel">
  <h2 class="panel-title" style="left:18px;top:24px;width:420px;line-height:25px;font-weight:400">Three steps To find property management companies near you:</h2>
  <ol class="steps">
    <li>Select your property type and zipcode</li>
    <li>Review property manager listings in your area</li>
    <li>Select and compare property managers</li>
  </ol>
  <a class="btn" style="left:169px;top:220px;width:144px;height:39px">Find Now
    <svg viewBox="0 0 12 12"><path d="M1 0l11 6-11 6z"/></svg></a>
</section>

<footer class="abs site-footer">
  <p class="copyright">Copyright © 2014, Venlox, All Rights Reserved</p>
  <ul class="footer-links">
    <li>Are you a Property Manager?</li><li>About Us</li><li>Contact Us</li><li>Terms of Use</li><li class="row-break"></li><li>Privacy Policy</li><li>Sitemap</li>
  </ul>
</footer>

</body>
</html>
```